Deliver a professional and engaging investment propsal.

I am appealing to highend smart investors and need a high quality, engaging and formal presentation in PDF.
StowBin: https://www.stowbin.net/sh/qwmtr48kelvan2x/ZZTrPHmLe7WqsnBFjQ4kR8vYt?dl=0
Text for project is in Stowbin called New Proposal Final
Along with past much older attempts of this job.
Any additional ideas to enable a better outcome would be appreicated.

```html
<!DOCTYPE html>
<html lang="en">
<head>
<meta charset="utf-8">
<title>Ridgeline Town Center — Proposal 2019</title>
<link href="https://fonts.googleapis.com/css2?family=Bebas+Neue&family=Lato:ital,wght@0,300;0,400;0,700;0,900;1,400;1,700&display=swap" rel="stylesheet">
<style>
:root{
  --blue:#1b72c0;
  --blue-deep:#155fa3;
  --ink:#1d1d1f;
  --body:#5b5f66;
  --rule:#c9ccd1;
  --canvas:#f3f3f4;
  --paper:#ffffff;
  --paper-grey:#e9eaec;
}
*{margin:0;padding:0;box-sizing:border-box}
html,body{width:867px;height:1200px;overflow:hidden;background:var(--canvas)}
body{position:relative;font-family:'Lato',sans-serif;color:var(--body)}
.page{position:absolute;width:376px;height:531px;background:var(--paper);box-shadow:0 1px 4px rgba(0,0,0,.18);overflow:hidden}
.page--cover{left:39px;top:50px}
.page--proposal{left:454px;top:50px}
.page--site{left:39px;top:618px;background:var(--paper-grey)}
.page--location{left:454px;top:618px}
.abs{position:absolute}

/* cover */
.cover-frame{left:133px;top:34px;width:212px;height:246px;border:2.5px solid var(--blue);border-left:none;z-index:2}
.cover-frame::before{content:"";position:absolute;left:0;top:-2.5px;width:2.5px;height:46px;background:var(--blue)}
.cover-title{left:38px;top:114px;font-family:'Lato',sans-serif;font-weight:900;font-size:35px;color:var(--blue);letter-spacing:.5px;z-index:3}
.cover-sub{left:39px;top:156px;font-family:'Bebas Neue',sans-serif;font-size:36px;line-height:1;color:var(--ink);letter-spacing:.3px;z-index:3}
.cover-year{left:39px;top:188px;font-family:'Bebas Neue',sans-serif;font-size:31px;color:var(--ink);z-index:3}
.cover-photo{left:0;top:251px;width:376px;height:178px;background:linear-gradient(135deg,#d9dde2 0%,#f4f5f6 45%,#b9bfc7 100%)}
.cover-band{left:0;top:429px;width:376px;height:102px;background:var(--blue)}
.cover-tab{left:31px;top:422px;width:84px;height:16px;background:#fff}

/* shared headings */
.kicker{font-weight:300;font-size:13px;color:#8a8e94;line-height:1}
.headline{font-weight:700;font-size:17px;color:var(--blue);line-height:1.05;letter-spacing:.2px}
.head-rule{height:2px;background:var(--blue)}
p,li{font-size:5.4px;line-height:1.45}
.lead-blue{font-style:italic;color:var(--blue)}
.bullets{list-style:none}
.bullets li{position:relative;padding-left:9px;margin-bottom:5px}
.bullets li::before{content:"";position:absolute;left:0;top:2px;width:3px;height:3px;background:var(--blue)}
.hl{color:var(--blue);font-weight:700;font-style:italic}
.section-label{font-style:italic;color:var(--blue);font-size:8.5px}

/* footer */
.footer-name{font-size:6.5px;letter-spacing:.3px;color:#444;top:510px;left:109px}
.footer-bar{left:198px;top:511px;width:151px;height:5px;background:var(--blue)}
.footer-bar--light{background:linear-gradient(90deg,#6fa6da 0 40%,var(--blue) 40%)}
.footer-line{left:0;top:519px;width:26px;height:1px;background:var(--blue-deep)}
.page-no{left:31px;top:514px;font-size:6.5px;font-weight:700;color:#444}

/* proposal page */
.divider{left:155px;top:156px;width:1px;height:332px;background:var(--rule)}
.plan{left:162px;top:324px;width:187px;height:163px;border:1px solid #d4d6d9;background:#fff}
.plan-map{left:14px;top:16px;width:159px;height:107px;background:linear-gradient(135deg,#a9b7a0,#cdd3c6 50%,#9aa995)}
.plan-thumbs{left:14px;top:126px;width:159px;height:24px;display:flex;gap:4px}
.plan-thumbs div{flex:1;background:linear-gradient(180deg,#b9c4cf,#a0806c)}
.plan-cap{left:0;width:187px;text-align:center;font-size:3.5px;color:#555}
.plan-bar{left:0;top:148px;width:187px;height:15px;background:var(--blue)}

/* site page */
.card{position:absolute;width:93px;height:98px;background:#fff;border-bottom:3px solid var(--blue);text-align:center}
.card-figure{margin-top:22px;font-family:'Bebas Neue',sans-serif;color:var(--blue);font-size:26px;line-height:1}
.card-figure--sm{font-size:17px;margin-top:20px}
.card-icon{margin-top:18px;height:30px}
.card p{font-size:4.3px;line-height:1.4;color:#6a6e74;padding:0 10px;margin-top:14px}
.card-icon + p{margin-top:6px}

/* location page */
.loc-frame{left:26px;top:26px;width:327px;height:472px;border:1.5px solid var(--blue)}
.loc-tab{left:26px;top:26px;width:140px;height:28px;background:var(--blue);color:#fff;font-weight:700;font-size:16px;letter-spacing:.4px;padding:5px 0 0 24px}
.loc-photo{left:13px;top:172px;width:160px;height:280px;background:linear-gradient(180deg,#b9c0c6 0%,#a59a86 40%,#8f7f67 100%)}
.loc-photo-top{left:13px;top:172px;width:160px;height:16px;background:var(--blue)}
.loc-photo-bottom{left:13px;top:440px;width:160px;height:12px;background:var(--blue)}
.loc-cap{left:13px;top:384px;width:160px;background:rgba(255,255,255,.9);font-size:3.4px;text-align:center;color:#333;padding:2px}
</style>
</head>
<body>

<section class="page page--cover">
  <div class="abs cover-photo" role="img" aria-label="Business team reviewing charts on a clipboard at a meeting table with coffee cups"></div>
  <div class="abs cover-band"></div>
  <div class="abs cover-tab"></div>
  <div class="abs cover-frame"></div>
  <h1 class="abs cover-title">PROPOSAL</h1>
  <div class="abs cover-sub">RIDGELINE TOWN CENTER</div>
  <div class="abs cover-year">2019</div>
</section>

<section class="page page--proposal">
  <div class="abs kicker" style="left:40px;top:60px">Joint Venture</div>
  <h2 class="abs headline" style="left:40px;top:72px">PROPOSAL</h2>
  <div class="abs head-rule" style="left:40px;top:93px;width:273px"></div>
  <p class="abs" style="left:40px;top:100px;width:295px">We have an incredible property, Ridgeline Business Park, located at 1180 State Route 40, Kessler County, Harlow Falls, North Dakota 58000 USA which we have fully funded with cash and now need a joint venture partner, buyer or lender to get this project to completion and producing a substantial profit we all can share.</p>

  <div class="abs section-label" style="left:40px;top:163px">Participation Options</div>
  <ul class="abs bullets" style="left:42px;top:180px;width:108px">
    <li>A joint venture partner would support all the costs developing the property without the <span class="hl">upfront costs</span> of the property purchase.</li>
    <li>All sales would be split to ensure both parties are paid out in such a way that both are paid out in full at the same time then a <span class="hl">50/50 profit</span> share split on all remaining sales.</li>
    <li>Contract drawn up <span class="hl">protecting</span> and <span class="hl">supporting</span> both parties on agreed terms.</li>
    <li>As a potential joint venture partner, I would cover the full property (57.7 acres) cost as mentioned of <span class="hl">$124,784</span> per acre (57.7 acres) <span class="hl">($7,200,000)</span></li>
    <li>Point venture partner to supply the development costs estimated to be around <span class="hl">$65,000</span> an acre estimated pending tender selection and additional refundable security bonds held with the Harlow Falls city on development works.</li>
    <li>Development costs could be in up to three stages to <span class="hl">lower outlay</span> and <span class="hl">limit exposure</span> if so desired, however it will take longer to complete and bring to market.</li>
    <li>A buyer can be fully supported by myself to oversee the full project and outcomes and support the budgets of construction and sales to get the <span class="hl">highest returns</span> for a small fee.</li>
    <li>Financing on excellent terms allowing <span class="hl">12 to 18 months</span> for income streams and could be linked to a joint venture option / profit share.</li>
  </ul>

  <div class="abs divider"></div>

  <p class="abs lead-blue" style="left:166px;top:175px;width:184px;font-size:7.4px;line-height:1.4">Our property is located on the best oil reserves in the world in North Dakota USA, with more oil than any other county in the Tallgrass Basin and with the lowest recoverable costs of $24 a barrel.</p>
  <p class="abs" style="left:166px;top:238px;width:182px;font-size:5.8px">We own the property and need a partner to develop the site and bring to the market at half the cost of competing business parks in the area.</p>
  <ul class="abs bullets" style="left:168px;top:270px;width:180px">
    <li>To purchase the property, you would need to contact me directly and I can introduce you to our realtor who will discount his commission from 6% to 5% which is a significant saving.</li>
  </ul>

  <div class="abs plan">
    <div class="abs plan-cap" style="top:3px">60 ACRE MIXED-USE DEVELOPMENT</div>
    <div class="abs plan-cap" style="top:8px;font-size:4.5px;font-weight:700;color:#222">RIDGELINE TOWN CENTER</div>
    <div class="abs plan-map" role="img" aria-label="Site plan of the mixed-use development showing lots, roads and green space"></div>
    <div class="abs plan-thumbs" role="img" aria-label="Three architectural renderings of planned hotel and retail buildings"><div></div><div></div><div></div></div>
    <div class="abs plan-bar"></div>
  </div>

  <div class="abs footer-line"></div>
  <div class="abs page-no">2</div>
  <div class="abs footer-line" style="left:42px;width:60px"></div>
  <div class="abs footer-name">RIDGELINE TOWN CENTER</div>
  <div class="abs footer-bar"></div>
</section>

<section class="page page--site">
  <div class="abs kicker" style="left:42px;top:62px">Major</div>
  <h2 class="abs headline" style="left:42px;top:74px">SITE CHANGE</h2>
  <div class="abs head-rule" style="left:42px;top:96px;width:271px"></div>
  <p class="abs" style="left:42px;top:107px;width:300px;font-size:5.8px">We purchased the property in 2013 for cash and without any additional debt, at the time we had Route 40 frontage just outside Harlow Falls city limits, south of town with a zoning of agricultural within Kessler County.</p>

  <div class="card" style="left:33px;top:160px">
    <div class="card-figure">2014</div>
    <p>2014 site zoning changed allowing a commercial zoning.</p>
  </div>
  <div class="card" style="left:141px;top:160px">
    <svg class="card-icon" viewBox="0 0 30 30" width="30" aria-hidden="true"><rect x="7" y="3" width="16" height="24" fill="var(--blue)"/><g fill="#fff"><rect x="9" y="6" width="3" height="3"/><rect x="13.5" y="6" width="3" height="3"/><rect x="18" y="6" width="3" height="3"/><rect x="9" y="11" width="3" height="3"/><rect x="13.5" y="11" width="3" height="3"/><rect x="18" y="11" width="3" height="3"/><rect x="9" y="16" width="3" height="3"/><rect x="18" y="16" width="3" height="3"/><rect x="13" y="20" width="4" height="7"/></g></svg>
    <p>Flag hotel site purchased 2014 now with the option to purchase the franchise license and build the hotel ourselves.</p>
  </div>
  <div class="card" style="left:250px;top:160px">
    <svg class="card-icon" viewBox="0 0 30 30" width="30" aria-hidden="true"><path d="M17 2 C14 8 11 11 11 15 a6 6 0 0 0 12 0 C23 11 20 8 17 2Z" fill="var(--blue)"/><path d="M3 21 C8 20 11 24 16 24 L25 22" fill="none" stroke="var(--blue)" stroke-width="2.4" stroke-linecap="round"/></svg>
    <p>In 2016 we were added into city limits which was a massive improvement to our site now taking advantage of confirmed city water and sewer, a great outcome.</p>
  </div>
  <div class="card" style="left:33px;top:276px">
    <div class="card-figure card-figure--sm">100 YARDS</div>
    <p>In 2016 the new bypass opened intersecting our highway front age just 100 yards away which brings all the traffic in the Tallgrass right past our site, which was a massive win for this project.</p>
  </div>
  <div class="card" style="left:141px;top:276px">
    <div class="card-figure card-figure--sm">$750,000</div>
    <p>Same commercial property listed across the road at $750,000 per acre retail at Linden Commons and other business parks average listings $550,00 per acre.</p>
  </div>
  <div class="card" style="left:250px;top:276px">
    <div class="card-figure card-figure--sm">2017-18</div>
    <p>In late 2017 we applied for full site development application and were approved in mid-2018 which again was a significant improvement to the project.</p>
  </div>

  <p class="abs" style="left:33px;top:398px;width:310px;font-size:5.8px">May 2018 full site infrastructure development approval which includes all roads and city services, this will trigger interest in the site from passing traffic and with a great marketing campaign will surely start sales coming in quickly once we break ground and start work.</p>
  <p class="abs" style="left:33px;top:428px;width:310px;font-size:5.8px">We also can buy the franchise license of the Prairie Rest hotel for additional income potential if desired.</p>

  <div class="abs footer-line"></div>
  <div class="abs page-no">2</div>
  <div class="abs footer-line" style="left:42px;width:62px"></div>
  <div class="abs footer-name" style="color:#333">RIDGELINE TOWN CENTER</div>
  <div class="abs footer-bar footer-bar--light" style="width:178px"></div>
</section>

<section class="page page--location">
  <div class="abs loc-frame"></div>
  <h2 class="abs loc-tab">LOCATION</h2>
  <p class="abs" style="left:40px;top:68px;width:304px">Our property is ideally located in Harlow Falls, United States of America, despite its humble beginnings, has suddenly found itself at the epicentre of the Tallgrass oil boom located in western North Dakota, the city has seen workers flood into the area over recent years to fill positions to support the growth.</p>
  <p class="abs" style="left:40px;top:95px;width:304px">Kessler County where Harlow Falls is located has more recoverable oil and gas at the lowest recoverable cost per barrel at $24, making it most affordable anywhere in the Tallgrass Basin, centrally located and very desirable area to establish a business and company headquarters.</p>
  <p class="abs lead-blue" style="left:40px;top:123px;width:304px">Harlow Falls is the crossroads whereby around 20,000 vehicles pass by our site each day travelling locally and between Northbrook where boom started and Easton an established town with relevant established support for business and infrastructure. Our project has highway frontage and is 100 yards away from the bypass intersection making it the best location in Kessler County for this type of project.</p>

  <div class="abs loc-photo" role="img" aria-label="Aerial photograph of the flat prairie site beside the highway and new bypass"></div>
  <div class="abs loc-photo-top"></div>
  <div class="abs loc-cap">60 acre development site — 2.7 acres sold already to the hotel group, now with a new bypass and inside the city limits.</div>
  <div class="abs loc-photo-bottom"></div>

  <p class="abs" style="left:190px;top:182px;width:155px">With billions invested into infrastructure in the past 5 years in and around the Tallgrass oil basin our project has become the beneficiary of a major new Harlow Falls bypass which intersects Route 40 just 100 yards south of our project, putting us on one of the busiest intersections in the Tallgrass. With this rapid growth we were included into the Harlow Falls city limits providing additional benefits to the overall success for our development including all city services.</p>
  <p class="abs" style="left:190px;top:249px;width:155px">Demand stems from the ongoing boom in oil and gas drilling in the area which is still in its infancy stages of life, North Dakota oil play and is expected to continue to grow well past 2050 based on obtainable reserves beneath the ground.</p>
  <div class="abs section-label" style="left:190px;top:294px">Additional location growth:</div>
  <ul class="abs bullets" style="left:191px;top:310px;width:155px">
    <li>Corvane 150 million-dollar Harlow Falls city investment 2018</li>
    <li>North Dakota is the nation's second-biggest oil producer</li>
    <li>Kessler County investment development</li>
    <li>Within the 100 yards of Ridgeline Business Park, directly across the road, commercial land is currently listed at $750,000 an acre at Linden Commons and many more locations up to $650,000 per acre. With an advantage over other sites in terms of a better location and much lower purchase and development costs the numbers don't lie, and we need to have pad ready to build lots to offer the market.</li>
    <li>Tallgrass traffic, north, south, east and west will have to travel right by our site making it the second busiest intersection in the basin area, giving us the best exposure to sell, promote and grow, this site can and will be the location for new business and growth, we need to develop the site now to move forward.</li>
  </ul>
  <p class="abs lead-blue" style="left:40px;top:464px;width:306px">With our obvious high exposure to potential buyers through the passing traffic and lower entry price point there is no doubt Ridgeline Town Center will become the place where business will want to build alongside a quality business like the Prairie Rest Extended Stay Hotel.</p>

  <div class="abs footer-line"></div>
  <div class="abs page-no">2</div>
  <div class="abs footer-line" style="left:42px;width:60px"></div>
  <div class="abs footer-name">RIDGELINE TOWN CENTER</div>
  <div class="abs footer-bar"></div>
</section>

</body>
</html>
```